Book cover design for Verses for Tillers and Tinkers, 30th Anniversary Revised Edition

Simple, clean book cover design for the 30th Anniversary Edition of "Verses for Tillers and Tinkers" by noted author Lucas Harrowgate. Mostly typographical design, but also with an integrated design icon that immediately captures and conveys the sense of "science and industry" (a gear inside a science beaker? Atoms revolving around a nucleus? Etc. This is where your creativity comes in, and will be a critical element of the final cover design).

Book cover will be printed in one color only (black/screened gray)

Book/cover trim size: 5 3/8" x 8 1/2 "

Cover elements (all of these must be present):

Title: Verses for Tillers and Tinkers
Author: Lucas Harrowgate
Reading/tag line: 30th Anniversary Revised Edition
Design element

*
Your design will be acknowledged in the book.

I look forward to seeing your submission!
Updates

Book/cover trim size is 5 3/8" x 8 1/2"

Industry/Entity Type

Industry

Requirements
Must have
• Cover elements (all of these must be present):
• Title: Verses for Tillers and Tinkers
• Author: Lucas Harrowgate
• Reading/tag line: 30th Anniversary Revised Edition
• Design element
Should not have
• No color -- black and grayscale only

```html
<!DOCTYPE html>
<html lang="en">
<head>
<meta charset="utf-8">
<title>Verses for Tillers and Tinkers — Lucas Harrowgate</title>
<link rel="stylesheet" href="https://fonts.googleapis.com/css2?family=Arimo:wght@400;700&family=Tinos&display=swap">
<style>
  :root {
    --band-gray: #636363;
    --paper: #ffffff;
    --ink: #000000;
    --emblem-light: #bdbdbd;
    --emblem-dark: #8a8a8a;
  }
  html, body {
    margin: 0;
    padding: 0;
    overflow: hidden;
    background: var(--paper);
  }
  .cover {
    position: relative;
    width: 759px;
    height: 1200px;
    background: var(--paper);
    overflow: hidden;
  }
  .top-band {
    position: absolute;
    left: 0; top: 0;
    width: 100%;
    height: 100px;
    background: var(--band-gray);
  }
  .title {
    position: absolute;
    left: 0; top: 262px;
    width: 100%;
    margin: 0;
    text-align: center;
    font-family: "Arimo", Arial, sans-serif;
    font-weight: 700;
    color: var(--ink);
    text-transform: uppercase;
    letter-spacing: -1.5px;
    line-height: 58px;
  }
  .title .line { display: block; }
  .title .major { font-size: 55px; }
  .title .minor { font-size: 39px; }
  .emblem {
    position: absolute;
    left: 255px; top: 478px;
    width: 248px;
    height: 248px;
    border-radius: 50%;
    background: radial-gradient(circle at 50% 50%, var(--emblem-light) 0%, var(--emblem-dark) 100%);
  }
  .tagline {
    position: absolute;
    left: 0; top: 780px;
    width: 100%;
    margin: 0;
    text-align: center;
    font-family: "Tinos", "Times New Roman", serif;
    font-weight: 400;
    font-size: 50px;
    line-height: 54px;
    color: var(--ink);
  }
  .tagline .line { display: block; }
  .bottom-band {
    position: absolute;
    left: 0; top: 1013px;
    width: 100%;
    height: 187px;
    background: var(--band-gray);
  }
  .author {
    position: absolute;
    left: 0; top: 1112px;
    width: 100%;
    margin: 0;
    text-align: center;
    font-family: "Arimo", Arial, sans-serif;
    font-weight: 400;
    font-size: 40px;
    line-height: 48px;
    letter-spacing: -0.5px;
    color: var(--paper);
    text-transform: uppercase;
  }
</style>
</head>
<body>
  <main class="cover">
    <div class="top-band"></div>

    <h1 class="title">
      <span class="line"><span class="major">Verses</span> <span class="minor">for</span></span>
      <span class="line"><span class="major">Tillers</span> <span class="minor">and</span> <span class="major">Tinkers</span></span>
    </h1>

    <div class="emblem" role="img" aria-label="Emblem of a gray gear with atomic orbits and electrons, symbolising science and industry"></div>

    <p class="tagline">
      <span class="line">30th Anniversary</span>
      <span class="line">Revised Edition</span>
    </p>

    <div class="bottom-band"></div>
    <p class="author">Lucas Harrowgate</p>
  </main>
</body>
</html>
```